Rebrand of 3 bottle labels for nail polish brand

The task is to make a rebranding of our current gel nail polish bottle design. We have become one of the leading european nail polish brand, so we want to improve the quality of the label design to a more scandinavian and minimalistic bottle design, which stille has to be recognisable and unique.

We have attached a more detailed description of the rebranding instructions for our gel polish bottles called "bottle task".
Updates

The Labels should not be just Black and White as stated. But should be mainly Black and White and then some of our color as explained in the uploaded file.

Target Market(s)

Girls and women age 18-55 Northern Europe

Industry/Entity Type

Cosmetic/ Nail Gel Polish

Colors

Designer to choose only greyscale colors for use in the design.

Requirements
Must have
• See attched design instruction
Nice to have
• Moderne, Minimalist, Recognizable and Unique look
Should not have
• Too many elements, too busy design

```html
<!DOCTYPE html>
<html lang="en">
<head>
<meta charset="utf-8">
<title>Velune label set</title>
<link href="https://fonts.googleapis.com/css2?family=Quicksand:wght@400;500&family=Nunito:wght@700;800&display=swap" rel="stylesheet">
<style>
:root{
  --board:#a7a8ab;
  --ink:#0a0a0a;
  --rose:#bf948c;
  --rose-light:#cca59e;
  --white:#ffffff;
}
*{margin:0;padding:0;box-sizing:border-box}
html,body{width:1200px;height:1200px;overflow:hidden;background:var(--board)}
body{position:relative;font-family:"Quicksand",sans-serif;color:var(--white)}
.label{position:absolute;overflow:hidden;background:var(--rose)}
.band-top{position:absolute;left:0;top:0;width:100%;background:var(--ink)}
.abs{position:absolute}
.wordmark{position:absolute;font-family:"Quicksand",sans-serif;font-weight:400;color:var(--white);line-height:1;transform:translateX(-50%);white-space:nowrap}
.wordmark sup{font-size:.18em;vertical-align:top;position:relative;top:.1em;margin-left:.05em}
.product-type{position:absolute;font-weight:400;text-transform:uppercase;line-height:1;transform:translateX(-50%);white-space:nowrap}
.cure-tab{position:absolute;background:var(--rose);border-radius:12px 12px 0 0;font-family:"Nunito",sans-serif;font-weight:800;text-align:center;white-space:nowrap}
.shade{position:absolute;font-family:"Nunito",sans-serif;font-weight:800;line-height:1;transform:translateX(-50%)}
.shade-number{position:absolute;font-family:"Nunito",sans-serif;font-weight:800;color:var(--rose-light);line-height:1;letter-spacing:-.04em}
.dash{position:absolute;border-top:1.4px dashed var(--white);height:0}
.leaf-mark{position:absolute;background:linear-gradient(160deg,#d4b3ad,#bf948c);border-radius:50% 6px 50% 6px}
.rule{position:absolute;width:1px;background:var(--white)}
.spec{position:absolute;font-weight:400;line-height:1;white-space:nowrap}
.fineprint{position:absolute;text-align:center;transform:translateX(-50%);white-space:nowrap;font-weight:500}
.fineprint b{font-family:"Nunito",sans-serif;font-weight:800}
.icons{position:absolute;display:flex;gap:4px}
.icons span{width:22px;height:21px;background:var(--white);border-radius:1px}
.remover .band-top{background:var(--white)}
.remover .wordmark{color:var(--rose)}
.remover .fineprint{color:var(--rose)}
</style>
</head>
<body>

<!-- Base coat, shade 01 -->
<section class="label" style="left:29px;top:181px;width:731px;height:196px">
  <div class="band-top" style="height:101px"></div>
  <div class="wordmark" style="left:151px;top:12px;font-size:52px">velune<sup>TM</sup></div>
  <div class="product-type" style="left:155px;top:69px;font-size:13px">Base Coat</div>
  <div class="cure-tab" style="left:78px;top:85px;width:157px;height:20px;font-size:15px;line-height:21px">SOAK OFF UV/LED</div>
  <div class="shade-number" style="left:2px;top:108px;font-size:82px">01</div>
  <div class="shade" style="left:158px;top:110px;font-size:13px">FLEXIBLE</div>
  <div class="dash" style="left:94px;top:131px;width:127px"></div>
  <div class="leaf-mark" role="img" aria-label="Leaf line icon for vegan formula" style="left:97px;top:136px;width:32px;height:36px"></div>
  <div class="rule" style="left:136px;top:135px;height:35px"></div>
  <div class="spec" style="left:142px;top:139px;font-size:11.5px">15ml e 0.5oz</div>
  <div class="spec" style="left:142px;top:156px;font-size:11.5px">Vegan Formula</div>
  <div class="dash" style="left:94px;top:174px;width:127px"></div>
  <div class="fineprint" style="left:530px;top:12px;font-size:4.4px;line-height:5.7px">
    <b>DIRECTIONS FOR USE (ENG):</b><br>Velune Base Coat must be applied in thin layers and cured in one of our Velune Lamps.<br>
    <b>ANVENDELSE (DK):</b><br>Velune Base Coat skal påføres i tynde lag og hærdes i en af vores Velune Lamper.<br>
    <b>CAUTION (ENG):</b><br>Keep out of reach of children. Discontinue use if irritation occurs.<br>Avoid direct sunlight or extreme exposure to LED or UV light.<br>
    <b>ADVARSEL (DK):</b><br>Opbevar utilgængeligt for børn. Stop din behandling, hvis produktet forudsager irritation.<br>Undgå direkte sollys eller udsættelse for LED eller UV.<br>
    <b>INGREDIENTS:</b><br>Acrylates Copolymer, Acrylated Aliphatic Urethane, Cellulose Acetate Butanoate,
  </div>
  <div class="fineprint" style="left:530px;top:117px;font-size:5.2px;line-height:7px">Dimethicone, Ceresine, wax , Pigment Red, Carbon<br>Black, Titanium dioxide, CI 77891<br><b>Made in Germany</b></div>
  <div class="icons" style="left:480px;top:141px"><span></span><span></span><span></span><span></span></div>
  <div class="fineprint" style="left:530px;top:171px;font-size:5.2px;line-height:7px">Nordlys Partners A/S - Lindelund 14, 2700 Ravnsby,<br>Denmark</div>
</section>

<!-- Base coat, shade 21 -->
<section class="label" style="left:29px;top:404px;width:731px;height:195px">
  <div class="band-top" style="height:100px"></div>
  <div class="wordmark" style="left:151px;top:11px;font-size:52px">velune<sup>TM</sup></div>
  <div class="product-type" style="left:155px;top:68px;font-size:13px">Base Coat</div>
  <div class="cure-tab" style="left:78px;top:84px;width:157px;height:20px;font-size:15px;line-height:21px">SOAK OFF UV/LED</div>
  <div class="shade-number" style="left:2px;top:107px;font-size:82px">21</div>
  <div class="shade" style="left:158px;top:109px;font-size:13px">PINK</div>
  <div class="dash" style="left:94px;top:130px;width:127px"></div>
  <div class="leaf-mark" role="img" aria-label="Leaf line icon for vegan formula" style="left:97px;top:135px;width:32px;height:36px"></div>
  <div class="rule" style="left:136px;top:134px;height:35px"></div>
  <div class="spec" style="left:142px;top:138px;font-size:11.5px">15ml e 0.5oz</div>
  <div class="spec" style="left:142px;top:155px;font-size:11.5px">Vegan Formula</div>
  <div class="dash" style="left:94px;top:173px;width:127px"></div>
  <div class="fineprint" style="left:530px;top:14px;font-size:4.4px;line-height:5.7px">
    <b>DIRECTIONS FOR USE (ENG):</b><br>Velune Color Coat must be applied in thin layers and cured in one of our Velune Lamps.<br>
    <b>ANVENDELSE (DK):</b><br>Velune Farver skal påføres i tynde lag og hærdes i en af vores Velune Lamper.<br>
    <b>CAUTION (ENG):</b><br>Keep out of reach of children. Discontinue use if irritation occurs.<br>Avoid direct sunlight or extreme exposure to LED or UV Light.<br>
    <b>ADVARSEL (DK):</b><br>Opbevar utilgængeligt for børn. Stop din behandling,<br>hvis produktet forudsager irritation. Undgå direkte sollys eller udsættelse for LED eller UV.<br>
    <b>INGREDIENTS:</b><br>Acrylates Copolymer, Acrylated Aliphatic Urethane, Cellulose Acetate Butanoate,<br>Dimethicone, Ceresine, wax , Pigment Red, Carbon Black, Titanium dioxide, CI 77891
  </div>
  <div class="fineprint" style="left:530px;top:117px;font-size:5.2px;line-height:7px">Dimethicone, Ceresine, wax , Pigment Red, Carbon<br>Black, Titanium dioxide, CI 77891<br><b>Made in Europe</b></div>
  <div class="icons" style="left:480px;top:141px"><span></span><span></span><span></span><span></span></div>
  <div class="fineprint" style="left:530px;top:171px;font-size:5.2px;line-height:7px">Nordlys Partners A/S - Lindelund 14, 2700 Ravnsby,<br>Denmark</div>
</section>

<!-- Gel polish remover -->
<section class="label remover" style="left:29px;top:620px;width:731px;height:398px">
  <div class="band-top" style="height:249px"></div>
  <div class="wordmark" style="left:157px;top:36px;font-size:70px">velune<sup>TM</sup></div>
  <div class="cure-tab" style="left:75px;top:170px;width:172px;height:79px;border-radius:18px 18px 0 0;font-family:'Nunito',sans-serif;font-size:29px;line-height:37px;padding-top:4px;color:var(--white)">Gel Polish<br>Remover</div>
  <div class="shade-number" style="left:-2px;top:228px;font-size:130px">12</div>
  <div class="dash" style="left:82px;top:285px;width:159px"></div>
  <div class="spec" style="left:90px;top:301px;font-size:21px">120ml e 4 fl.oz</div>
  <div class="dash" style="left:82px;top:338px;width:159px"></div>
  <div class="fineprint" style="left:530px;top:27px;font-size:8.5px;line-height:10.4px;font-weight:400">
    <b>DIRECTIONS FOR USE (ENG):</b><br>To remove the Velune, soak a lint free wipe with the Velune Polish Remover,<br>place the saturated wipe on the nail and wrap each nail in foil for 15 minutes.<br>Remove the foil and peel off the gel polish remover. Re-apply if needed.<br>We recommend that you moisturise your nails after this treatment<br>
    <b>ANVENDELSE (DK):</b><br>For at fjerne Velune, skal du væde en fnugfri wipe ind i Velune Neglelakfjerner,<br>hvorefter du placere din fnugfri wipe på neglen og klemmer den fast i<br>15 minutter med sølvpapir og negleklips.<br>Fjern herefter foliet og skrab din gellak af med en neglebåndsskubber.<br>Gentag hvis nødvendigt. Vi anbefaler negleolie efter din behandling.<br>
    <b>CAUTION (ENG):</b><br>Keep out of the reach of children<br>Discontinue use if sensitivity or irritation occurs<br>
    <b>ADVARSEL (DK):</b><br>Opbevares utilgængeligt for børn<br>Stop din behandling hvis følsomhed eller irritation opstår<br>
    <b>INGREDIENTS:</b><br>Ethyl acetate, n-butyl acetate, Methyl Ethyl ketone,<br>Acetone, Isopropyl alcohol, glycerin
  </div>
  <div class="fineprint" style="left:530px;top:331px;font-size:8.5px;line-height:10.4px;color:var(--white)"><b>Nordlys Partners A/S - Lindelund 14, 2700 Ravnsby,<br>Denmark</b></div>
</section>

<!-- Front panel, base coat shade 1 -->
<section class="label" style="left:803px;top:646px;width:357px;height:314px">
  <div class="band-top" style="height:161px"></div>
  <div class="wordmark" style="left:177px;top:26px;font-size:82px">velune<sup>TM</sup></div>
  <div class="product-type" style="left:175px;top:110px;font-size:21px">Base Coat</div>
  <div class="cure-tab" style="left:49px;top:133px;width:253px;height:28px;border-radius:16px 16px 0 0;font-size:24px;line-height:32px">SOAK OFF UV/LED</div>
  <div class="shade-number" style="left:2px;top:168px;font-size:125px">1</div>
  <div class="shade" style="left:180px;top:176px;font-size:21px">FLEXIBLE</div>
  <div class="dash" style="left:76px;top:211px;width:205px;border-top-width:2px"></div>
  <div class="leaf-mark" role="img" aria-label="Leaf line icon for vegan formula" style="left:82px;top:218px;width:50px;height:56px"></div>
  <div class="rule" style="left:143px;top:216px;height:56px"></div>
  <div class="spec" style="left:153px;top:222px;font-size:18px">15ml e 0.5oz</div>
  <div class="spec" style="left:153px;top:250px;font-size:18px">Vegan Formula</div>
  <div class="dash" style="left:76px;top:281px;width:205px;border-top-width:2px"></div>
</section>

</body>
</html>
```